La Brasa Dorada – CPG Website with WordPress - Store Locator: WP Maps plugin

Harlow Pantry Company is a startup consumer packaged goods (CPG) brand launching its flagship product line — La Brasa Dorada. We’re seeking a talented web designer to create a bold, professional, mobile-optimized website using WordPress with a WP Maps store locator to help customers find local retailers.

Our goal is to build a strong online presence that supports both retail growth and direct-to-consumer sales.

See La Brasa _Website_Design_Brief word document.

The website URL is https://labrasadorada.example/

Target Market(s)

Consumers of gourmet salsa

Industry/Entity Type

Consumer Packaged Goods - Salsa manufacturer.

Coding

Coded - Design and coding required

Number of Pages Required

5+ page

Requirements
Must have
• The design of the La Brasa Dorada website shall emulate the clean, polished aesthetic of Quillby.example.

```html
<!DOCTYPE html>
<html lang="en">
<head>
<meta charset="utf-8">
<title>La Brasa Dorada – All Natural Salsa</title>
<link href="https://fonts.googleapis.com/css2?family=Lobster+Two:ital,wght@0,700;1,700&family=Montserrat:wght@400;500;600&display=swap" rel="stylesheet">
<style>
:root{
  --red:#cc1f1f;
  --yellow:#f8c317;
  --yellow-deep:#f3b60f;
  --ink:#111111;
  --text:#6b6b6b;
  --card:#f2f2f2;
  --cream:#fcf8ee;
  --orange:#f0a02a;
  --green:#8aa84a;
  --line:#d9d9d9;
}
*{box-sizing:border-box;margin:0;padding:0}
html,body{width:1200px;height:3059px;overflow:hidden;background:#fff}
body{position:relative;font-family:"Montserrat",sans-serif;color:var(--ink)}
.abs{position:absolute}
.display{font-family:"Lobster Two",cursive;font-weight:700;font-style:italic}

/* header */
.site-header{position:absolute;left:0;top:0;width:1200px;height:107px;background:#fff}
.nav{position:absolute;top:48px;display:flex;gap:21px;font-size:14px;font-weight:500;letter-spacing:.2px}
.nav-left{left:153px}
.nav-right{left:773px}
.brand{position:absolute;left:500px;top:28px;width:200px;text-align:center;font-family:"Lobster Two",cursive;font-weight:700;font-size:52px;color:var(--red);line-height:1}

/* hero */
.hero{position:absolute;left:0;top:107px;width:1200px;height:667px;background:linear-gradient(180deg,var(--yellow) 0%,var(--yellow-deep) 100%)}
.hero-band{position:absolute;left:0;top:774px;width:1200px;height:12px;background:var(--red)}
.hero-title{position:absolute;left:0;top:190px;width:1200px;text-align:center;font-size:64px;line-height:70px;color:var(--ink)}
.hero-sub{position:absolute;left:0;top:350px;width:1200px;text-align:center;font-size:15px}
.btn{position:absolute;height:48px;border-radius:24px;display:flex;align-items:center;justify-content:center;font-size:15px;font-weight:500}
.btn-red{background:var(--red);color:#fff}
.btn-outline{border:2px solid var(--ink);color:var(--ink)}
.ph{position:absolute}

/* recipe */
.recipe-img{left:128px;top:991px;width:422px;height:384px;border-radius:16px;background:linear-gradient(135deg,#6f6f6f,#9b7b4a 45%,#5d8a3c 70%,#3a3a3a)}
.recipe-title{left:600px;top:998px;font-size:40px;color:var(--ink)}
.recipe-text{left:600px;top:1056px;width:470px;font-size:14.5px;line-height:22.3px;color:var(--text)}
.stats{left:598px;top:1228px;display:flex}
.stat{text-align:center;font-size:13.5px;padding:0 16px;border-left:1px solid var(--line);line-height:22px}
.stat:first-child{border-left:0;padding-left:0}
.stat b{font-weight:500;display:block}
.arrow{position:absolute;width:48px;height:48px;border-radius:50%;display:flex;align-items:center;justify-content:center}

/* products */
.section-title{position:absolute;left:0;width:1200px;text-align:center;font-size:40px}
.section-sub{position:absolute;left:270px;width:660px;text-align:center;font-size:14.5px;line-height:22px;color:var(--text)}
.product{position:absolute;top:1656px;width:273px;height:291px;border-radius:20px;background:var(--card)}
.jar{position:absolute;top:-58px;left:54px;width:165px;height:270px;border-radius:40px 40px 50px 50px}
.p-name{position:absolute;left:27px;top:228px;font-size:16.5px}
.p-rate{position:absolute;left:27px;top:252px;font-size:14px;font-weight:500;display:flex;align-items:center;gap:8px}
.stars{color:var(--orange);letter-spacing:1px;font-size:14px}
.cart{position:absolute;left:201px;top:225px;width:50px;height:50px;border-radius:50%;display:flex;align-items:center;justify-content:center}

/* reviews */
.reviews{position:absolute;left:0;top:2045px;width:1200px;height:585px;background:linear-gradient(180deg,var(--cream),#fff)}
.review{position:absolute;top:2178px;width:463px;height:270px;background:#fff;border-radius:20px;box-shadow:0 4px 20px rgba(0,0,0,.05);padding:24px 25px}
.review h3{font-size:16.5px;font-weight:500}
.review .stars{font-size:26px;letter-spacing:0;margin-top:4px;display:block}
.review p{font-size:14.5px;line-height:22.3px;color:var(--text);margin-top:6px}
.author{display:flex;align-items:center;gap:14px;margin-top:14px}
.avatar{width:68px;height:68px;border-radius:50%;background:linear-gradient(135deg,#8a6a55,#3b3b4a)}
.author span{font-size:21px}

/* social banner */
.social{position:absolute;left:89px;top:2642px;width:1021px;height:85px;border-radius:43px;background:linear-gradient(90deg,#f9a34a,#e4553d 35%,#a23fa6 65%,#5a55cf);display:flex;align-items:center;justify-content:center;color:#fff;font-size:38px}

/* footer */
.footer-brand{left:89px;top:2840px;font-family:"Lobster Two",cursive;font-weight:700;font-size:62px;color:var(--red);line-height:1}
.f-col{position:absolute;top:2822px;font-size:15px;color:var(--text);line-height:31px}
.pay{position:absolute;width:55px;height:36px;border-radius:7px}
.rule{left:89px;top:2991px;width:1021px;height:1px;background:var(--line)}
.copy{left:0;top:3014px;width:1200px;text-align:center;font-size:14px;color:var(--text)}
</style>
</head>
<body>

<header class="site-header">
  <nav class="nav nav-left"><span>PRODUCT</span><span>WHERE TO BUY</span><span>RECIPE</span></nav>
  <div class="brand">La Brasa</div>
  <nav class="nav nav-right"><span>ABOUT US</span><span>REVIEWS</span><span>CONTACT US</span></nav>
</header>

<section class="hero"></section>
<svg class="abs" style="left:0;top:107px" width="1200" height="680" aria-hidden="true">
  <g stroke="#1a1a1a" stroke-width="2" fill="none">
    <line x1="44" y1="0" x2="44" y2="667"/>
    <line x1="1154" y1="0" x2="1154" y2="667"/>
    <line x1="0" y1="44" x2="1200" y2="44"/>
    <line x1="0" y1="621" x2="1200" y2="621"/>
  </g>
</svg>
<div class="hero-band"></div>
<h1 class="hero-title display">Welcome To<br>Turn Up the Heat Naturally.</h1>
<p class="hero-sub">Gourmet, all-natural salsa made to spice up your snacks, meals,and moments.</p>
<div class="btn btn-red" style="left:418px;top:389px;width:142px">Shop Now</div>
<div class="btn btn-outline" style="left:570px;top:389px;width:212px">Find a Store Near You</div>
<div class="ph" role="img" aria-label="Three salsa jars: habanero, verde and all natural" style="left:287px;top:475px;width:628px;height:410px;border-radius:60px 60px 40px 40px;background:linear-gradient(90deg,#c8432a 0%,#d85d2b 30%,#9dbb4f 35%,#a9c25a 65%,#e2782c 70%,#f0a237 100%)"></div>
<div class="ph" role="img" aria-label="Red chili peppers, garlic and peppercorns" style="left:930px;top:665px;width:270px;height:170px;border-radius:80px 20px 80px 40px;background:linear-gradient(120deg,#c9141a,#a11016 60%,#6f8e3a)"></div>

<div class="ph recipe-img" role="img" aria-label="Bowl of slow cooker salsa beef with rice, avocado and salad"></div>
<h2 class="abs recipe-title display">Slow Cooker Salsa Beef</h2>
<p class="abs recipe-text">This Slow Cooker Salsa Beef is a weeknight lifesaver that's equal parts hearty, flavorful, and hands-off. Just a handful of ingredients including ground beef, onions, bell peppers, and bold seasonings come together in the slow cooker for a dish that practically makes itself. Stir in your favorite jar of La Brasa salsa, and let the flavors simmer all day into a saucy, savory blend with just the right amount of kick.</p>
<div class="abs stats">
  <div class="stat" style="color:var(--red)">PREP TIME:<b>10 MINS</b></div>
  <div class="stat" style="color:var(--orange)">COOK TIME:<b>8 HRS</b></div>
  <div class="stat" style="color:var(--green)">TOTAL TIME:<b>8 HRS 10 MIN</b></div>
  <div class="stat" style="color:#e0542a">SERVING:<b>4</b></div>
</div>
<div class="btn btn-red" style="left:600px;top:1302px;width:154px">View Recipe</div>
<div class="arrow" style="left:764px;top:1302px;background:#f2f2f2"><svg width="10" height="10" viewBox="0 0 10 10"><path d="M6.5 1.5 3 5l3.5 3.5" stroke="#111" stroke-width="1.8" fill="none"/></svg></div>
<div class="arrow" style="left:815px;top:1302px;background:#f2f2f2"><svg width="10" height="10" viewBox="0 0 10 10"><path d="M3.5 1.5 7 5 3.5 8.5" stroke="#111" stroke-width="1.8" fill="none"/></svg></div>

<h2 class="section-title display" style="top:1474px">All Natural. All Flavor</h2>
<p class="section-sub" style="top:1529px">Say goodbye to boring dips. Our salsas are handcrafted in small batches using real, clean ingredients — no preservatives, no shortcuts, just bold flavor in every bite.</p>

<div class="product" style="left:150px">
  <div class="jar" role="img" aria-label="All natural salsa jar" style="background:linear-gradient(180deg,#d9b54a 0 14%,#d9542a 14%,#f0a237 60%,#c8432a)"></div>
  <div class="p-name">All natural Salsa</div>
  <div class="p-rate"><span class="stars">★★★★★</span>4.8</div>
  <div class="cart" style="background:var(--red)"><svg width="22" height="22" viewBox="0 0 24 24"><path d="M3 4h3l2.2 10h10l2-7H7" stroke="#fff" stroke-width="2.2" fill="none"/><circle cx="9" cy="19" r="1.8" fill="#fff"/><circle cx="17" cy="19" r="1.8" fill="#fff"/></svg></div>
</div>
<div class="product" style="left:463px;top:1653px">
  <div class="jar" role="img" aria-label="Verde salsa jar" style="background:linear-gradient(180deg,#d9b54a 0 14%,#9dbb4f 14%,#b3c964 60%,#8aa84a)"></div>
  <div class="p-name">Verde Salsa</div>
  <div class="p-rate"><span class="stars">★★★★★</span>4.8</div>
  <div class="cart" style="background:var(--yellow)"><svg width="22" height="22" viewBox="0 0 24 24"><path d="M3 4h3l2.2 10h10l2-7H7" stroke="#fff" stroke-width="2.2" fill="none"/><circle cx="9" cy="19" r="1.8" fill="#fff"/><circle cx="17" cy="19" r="1.8" fill="#fff"/></svg></div>
</div>
<div class="product" style="left:776px">
  <div class="jar" role="img" aria-label="Habanero salsa jar" style="background:linear-gradient(180deg,#d9b54a 0 14%,#c8322a 14%,#d9542a 60%,#b02a22)"></div>
  <div class="p-name">Habanero Salsa</div>
  <div class="p-rate"><span class="stars">★★★★★</span>4.8</div>
  <div class="cart" style="background:var(--ink)"><svg width="22" height="22" viewBox="0 0 24 24"><path d="M3 4h3l2.2 10h10l2-7H7" stroke="#fff" stroke-width="2.2" fill="none"/><circle cx="9" cy="19" r="1.8" fill="#fff"/><circle cx="17" cy="19" r="1.8" fill="#fff"/></svg></div>
</div>

<section class="reviews"></section>
<h2 class="section-title display" style="top:2106px">Clients Reviews</h2>
<article class="review" style="left:122px">
  <h3>Delicious! Can't Find It!</h3>
  <span class="stars">★★★★★</span>
  <p>Say goodbye to bland, factory-made salsas. At La Brasa, we believe great taste starts with great ingredients-that's why every jar of our salsa made with farm fresh tomatoes hand-picked chilies, and a blend of herbs</p>
  <div class="author"><div class="avatar" role="img" aria-label="Customer portrait"></div><span class="display">Marco Delgado</span></div>
</article>
<article class="review" style="left:614px">
  <h3>Hands Down Our Favorite Salsa!</h3>
  <span class="stars">★★★★★</span>
  <p>Say goodbye to bland, factory-made salsas. At La Brasa, we believe great taste starts with great ingredients-that's why every jar of our salsa made with farm fresh tomatoes hand-picked chilies, and a blend of herbs</p>
  <div class="author"><div class="avatar" role="img" aria-label="Customer portrait"></div><span class="display">Marco Delgado</span></div>
</article>
<div class="arrow" style="left:539px;top:2486px;width:57px;height:57px;background:#e6e6e6"><svg width="12" height="12" viewBox="0 0 10 10"><path d="M6.5 1.5 3 5l3.5 3.5" stroke="#111" stroke-width="1.8" fill="none"/></svg></div>
<div class="arrow" style="left:603px;top:2486px;width:57px;height:57px;background:var(--red)"><svg width="12" height="12" viewBox="0 0 10 10"><path d="M3.5 1.5 7 5 3.5 8.5" stroke="#fff" stroke-width="1.8" fill="none"/></svg></div>

<div class="social display">Follow La Brasa on Picturegram</div>

<footer>
  <div class="abs footer-brand">La Brasa</div>
  <div class="f-col" style="left:372px">Product<br>Where to Buy<br>Recipe</div>
  <div class="f-col" style="left:553px">About Us<br>Reviews<br>Contact Us</div>
  <div class="f-col" style="left:725px">Privacy Policy<br>Shipping Policy<br>Terms &amp; Conditions</div>
  <div class="pay" style="left:937px;top:2826px;background:#e6e6e6"></div>
  <div class="pay" style="left:996px;top:2826px;background:#1f4fb5"></div>
  <div class="pay" style="left:1055px;top:2826px;background:#222"></div>
  <div class="pay" style="left:937px;top:2866px;background:#e6e6e6"></div>
  <div class="pay" style="left:996px;top:2866px;background:#2a73d0"></div>
  <div class="abs rule"></div>
  <p class="abs copy">© Copyright 2025, La Brasa Dorada All Natural Salsa, All Rights Reserved</p>
</footer>

</body>
</html>
```